Innovative Freezer Label Design

Create a versatile and innovative freezer label design with universal appeal, suitable for different functionalities. The design should cater to a diverse audience, including those who freeze meals for meal prepping, batch cooking, and the restaurant industry. Our vision is a visually striking and distinctive design that embodies simplicity.

Example "our current labels feature essential details like "Contents" and "Date." We recognize these as crucial points of information. Currently, the challenge lies in creating various labels for different marketplaces, considering language barriers. A proposed solution involves the integration of universal icons to replace specific words, promoting practicality for international sales."

Kindly note that design concepts should not be restricted to our current product, brand guideline, logo, or the provided example.

Our goal is not only product differentiation but also increased sales through a blend of functionality and aesthetics.

The following are examples of freezer labels designs. Kindly do not restrict your designs to the examples. The designs must be universal (for language barrier purposes)

Examples:
https://www.snaprovel.co.uk/pin/5820174630298837415/
https://www.snaprovel.co.uk/pin/5820174630298837419/
https://www.snaprovel.co.uk/pin/5820174630298837408/
https://www.snaprovel.co.uk/pin/5820174630298837322/
https://www.snaprovel.co.uk/pin/5820174630298898764/

Please reach out if you have any questions.

Thank you

```html
<!DOCTYPE html>
<html lang="en">
<head>
<meta charset="utf-8">
<title>Kelvane Freezer Labels</title>
<link rel="stylesheet" href="https://fonts.googleapis.com/css2?family=Crimson+Pro:wght@600&family=Source+Sans+3:wght@400&display=swap">
<style>
  :root {
    --bg-dark: #9d7049;
    --bg-light: #e2bb9c;
    --label-white: #ffffff;
    --sage: #8fa8a0;
    --sage-soft: #dfe7e4;
    --ink: #33444f;
    --caption: #56646c;
  }
  * { margin: 0; padding: 0; box-sizing: border-box; }
  html, body { width: 1200px; height: 1200px; overflow: hidden; }
  body {
    background: linear-gradient(225deg, var(--bg-light) 0%, #c4956e 40%, var(--bg-dark) 100%);
    position: relative;
    font-family: "Source Sans 3", "Helvetica Neue", Arial, sans-serif;
  }
  .freezer-label {
    position: absolute;
    width: 460px;
    background: var(--label-white);
    border-radius: 8px;
    box-shadow: 0 10px 24px rgba(70, 40, 15, 0.28);
    overflow: hidden;
  }
  .freezer-label--short { left: 120px; top: 295px; height: 301px; }
  .freezer-label--tall  { left: 620px; top: 295px; height: 611px; }

  .label-header { position: absolute; left: 0; top: 0; width: 460px; height: 100px; }
  .brand-name {
    position: absolute;
    left: 0; top: 22px; width: 460px;
    text-align: center;
    font-family: "Crimson Pro", Georgia, serif;
    font-weight: 600;
    font-size: 36px;
    letter-spacing: 2px;
    color: var(--ink);
  }
  .contents-rule {
    position: absolute;
    left: 40px; width: 380px; height: 2px;
    background: linear-gradient(90deg, rgba(143,168,160,0), var(--sage) 30%, var(--sage) 70%, rgba(143,168,160,0));
  }
  .field-caption {
    position: absolute;
    left: 0; width: 460px;
    text-align: center;
    font-size: 11.5px;
    letter-spacing: 0.3px;
    color: var(--caption);
  }
  .date-box { position: absolute; left: 137px; width: 186px; height: 64px; }

  .freezer-label--short .contents-rule { top: 170px; }
  .freezer-label--short .caption-contents { top: 176px; }
  .freezer-label--short .caption-date { top: 197px; }
  .freezer-label--short .date-box { top: 220px; }

  .freezer-label--tall .contents-rule { top: 381px; }
  .freezer-label--tall .caption-contents { top: 387px; }
  .freezer-label--tall .caption-date { top: 505px; }
  .freezer-label--tall .date-box { top: 528px; }
</style>
</head>
<body>

<svg width="0" height="0" style="position:absolute" aria-hidden="true">
  <defs>
    <linearGradient id="header-strip" x1="0" x2="1" y1="0" y2="0">
      <stop offset="0" stop-color="#ffffff"/>
      <stop offset="0.28" stop-color="#9fb5ad"/>
      <stop offset="0.72" stop-color="#9fb5ad"/>
      <stop offset="1" stop-color="#ffffff"/>
    </linearGradient>
    <linearGradient id="date-frame" x1="0" x2="0" y1="0" y2="1">
      <stop offset="0" stop-color="#8fa8a0"/>
      <stop offset="0.55" stop-color="#8fa8a0"/>
      <stop offset="1" stop-color="#8fa8a0" stop-opacity="0"/>
    </linearGradient>
    <symbol id="label-tab" viewBox="0 0 460 100">
      <rect x="20" y="0" width="420" height="44" fill="url(#header-strip)"/>
      <rect x="20" y="0" width="420" height="12" fill="#ffffff" opacity="0.35"/>
      <rect x="132" y="-20" width="196" height="114" rx="22" fill="#8fa8a0"/>
      <rect x="146" y="-20" width="168" height="101" rx="16" fill="#ffffff"/>
    </symbol>
    <symbol id="date-field" viewBox="0 0 186 64">
      <path d="M2 64 V22 Q2 2 22 2 H164 Q184 2 184 22 V64" fill="none" stroke="url(#date-frame)" stroke-width="2.5"/>
      <line x1="66" y1="30" x2="66" y2="48" stroke="#8fa8a0" stroke-width="2"/>
      <line x1="118" y1="30" x2="118" y2="48" stroke="#8fa8a0" stroke-width="2"/>
    </symbol>
  </defs>
</svg>

<section class="freezer-label freezer-label--short">
  <svg class="label-header" viewBox="0 0 460 100" aria-hidden="true"><use href="#label-tab"/></svg>
  <div class="brand-name">Kelvane</div>
  <div class="contents-rule"></div>
  <div class="field-caption caption-contents">CONTENTS</div>
  <div class="field-caption caption-date">DATE</div>
  <svg class="date-box" viewBox="0 0 186 64" aria-hidden="true"><use href="#date-field"/></svg>
</section>

<section class="freezer-label freezer-label--tall">
  <svg class="label-header" viewBox="0 0 460 100" aria-hidden="true"><use href="#label-tab"/></svg>
  <div class="brand-name">Kelvane</div>
  <div class="contents-rule"></div>
  <div class="field-caption caption-contents">CONTENTS</div>
  <div class="field-caption caption-date">DATE</div>
  <svg class="date-box" viewBox="0 0 186 64" aria-hidden="true"><use href="#date-field"/></svg>
</section>

</body>
</html>
```